Brochure for Specialist Divorce Support

1. I want an A4 three fold brochure or DL to promote my business and services.
My market are people going through divorce and are usually feeling very overwhelmed and therefore not functioning very well - both men and women, age early forties,
2. Colours – variety of blues and lime greens but you choose if you need a contrast e.g. orange
3. Images – happy single families
4. Theme - could you make it around water please - soothing
5. Logos – HWN &; HWT (I will attach)
6. I have a lot of content so maybe not too busy but still professional feel +
warm and reassuring
7. I'm attaching -

- a draft brochure I put together using a Microsoft template
- a word document with extra details
- plus two logos to do with my qualifications
- and some images for you to choose from

7. I want to use this as a template for some other brochures -> more work for
the winner.

Target Market(s)

Men and women usually in their early forties with primary school aged children i.e 5 to 12 years old.
They are going through a divorce and very upset, Maybe losing contact with their children and their way of life as they know it is disappearing. They are in turmoil and not functioning as well as they usually do.

Industry/Entity Type

Business

Font styles to use
Sans Serif

Colors
34a7d7
abd037
3277b5

Requirements
Must have
• I want the brochure to be three folds with the center the full A4
• Could you make the theme around water please.
• I will upload some photos for you to use if you want,

```html
<!DOCTYPE html>
<html lang="en">
<head>
<meta charset="utf-8">
<title>Specialist Divorce Support – Trifold Brochure</title>
<link rel="stylesheet" href="https://fonts.googleapis.com/css2?family=Open+Sans:ital,wght@0,400;0,600;0,700;0,800;1,400;1,600;1,700&display=swap">
<style>
  :root{
    --blue:#3277b5;
    --sky:#34a7d7;
    --lime:#abd037;
    --navy:#1f5d94;
    --pale:#e3f3fb;
    --paler:#f3fafd;
    --ink:#3a4a58;
    --white:#ffffff;
    --stage:#e9edf0;
  }
  *{box-sizing:border-box;margin:0;padding:0}
  html,body{width:1200px;height:2400px;overflow:hidden}
  body{background:var(--stage);font-family:"Open Sans",Arial,sans-serif;color:var(--ink);position:relative}
  .spread{position:absolute;left:60px;width:1080px;height:764px;display:flex;background:var(--white);box-shadow:0 6px 24px rgba(30,50,70,.18)}
  .spread--outside{top:290px}
  .spread--inside{top:1346px}
  .panel{position:relative;width:360px;height:764px;overflow:hidden}
  .panel + .panel{border-left:1px solid rgba(0,0,0,.05)}
  .photo{position:absolute}
  .swoosh{position:absolute;left:0;width:100%}

  /* ---------- outside: flap ---------- */
  .flap{background:linear-gradient(180deg,var(--pale),var(--paler) 60%)}
  .flap__body{position:absolute;top:34px;left:30px;right:26px}
  .flap__title{font-style:italic;font-weight:700;color:var(--blue);font-size:19px;margin-bottom:12px}
  .ticks{list-style:none}
  .ticks li{position:relative;padding-left:16px;font-size:11.5px;line-height:1.45;margin-bottom:6px}
  .ticks li::before{content:"";position:absolute;left:0;top:5px;width:7px;height:7px;border-radius:50%;background:var(--lime)}
  .flap__note{margin-top:14px;font-style:italic;font-weight:600;color:var(--blue);font-size:13px;line-height:1.45}
  .flap .photo{left:0;bottom:0;width:360px;height:270px;background:linear-gradient(180deg,#9fd4ee 0%,#4fb0da 45%,#e9d9b8 78%,#d8c29b 100%)}

  /* ---------- outside: back ---------- */
  .back{background:var(--white)}
  .back__circle{position:absolute;top:30px;left:105px;width:150px;height:150px;border-radius:50%;border:5px solid var(--sky);background:radial-gradient(circle at 50% 40%,#cfe5f2,#8fb7d2 70%,#6c93b0)}
  .back__body{position:absolute;top:196px;left:30px;right:28px}
  .section-title{font-weight:800;color:var(--blue);font-size:16px;letter-spacing:.5px;text-align:center;margin-bottom:10px}
  .back__foot{position:absolute;left:0;bottom:0;width:360px;height:250px}
  .back__foot svg{position:absolute;inset:0}
  .badges{position:absolute;top:70px;left:34px;display:flex;gap:26px;align-items:center}
  .badge{display:flex;align-items:center;gap:6px;font-weight:700;font-size:15px;color:var(--blue)}
  .badge__square{width:16px;height:16px;background:var(--lime)}
  .badge__circle{width:16px;height:16px;border-radius:50%;background:var(--sky)}
  .contact{position:absolute;top:118px;left:34px;right:30px;color:var(--white);font-size:11px;line-height:1.5}
  .contact__name{font-weight:700;font-size:13px}
  .web{position:absolute;left:0;bottom:18px;width:100%;padding:7px 30px;background:rgba(255,255,255,.92);color:var(--navy);font-weight:700;font-size:13px}

  /* ---------- outside: cover ---------- */
  .cover{background:var(--blue)}
  .cover .photo{top:0;left:0;width:360px;height:500px;background:linear-gradient(160deg,#c9d88a 0%,#9fbf63 25%,#d9b79a 55%,#b88f78 80%,#8f7a74 100%)}
  .brand{position:absolute;top:26px;right:26px;display:flex;align-items:center;gap:6px;font-weight:700;font-size:16px;color:var(--white)}
  .brand__circle{width:14px;height:14px;border-radius:50%;background:var(--white)}
  .cover__text{position:absolute;top:520px;left:30px;right:26px;color:var(--white)}
  .cover__title{font-weight:800;font-size:21px;letter-spacing:.3px;margin-bottom:10px}
  .cover__tag{font-style:italic;font-size:18px;line-height:1.35}
  .cover .web{bottom:34px;background:var(--white)}

  /* ---------- inside ---------- */
  .inside-panel{background:var(--white)}
  .inside-panel .photo{top:0;left:0;width:360px;height:240px}
  .photo--sea{background:linear-gradient(180deg,#eaf6fc 0%,#bfe2f3 45%,#7cc3e4 75%,#5aa9cf 100%)}
  .photo--family{background:linear-gradient(180deg,#8ecbeb 0%,#cfe9f6 50%,#e8e1d0 80%,#d6c6a7 100%)}
  .photo--sunset{background:linear-gradient(180deg,#7e8fa6 0%,#c9a27c 45%,#e8b46a 60%,#5d6f86 100%)}
  .goals{position:absolute;top:40px;left:28px;right:28px;font-style:italic;font-weight:700;color:var(--navy);font-size:15px;line-height:1.45;text-align:center}
  .inside-body{position:absolute;top:268px;left:28px;right:26px;font-size:11px;line-height:1.5}
  .lead{font-weight:700;color:var(--navy);font-size:13px;margin-bottom:10px}
  .stage{margin-bottom:12px}
  .stage__head{display:flex;align-items:flex-start;gap:8px;margin-bottom:4px}
  .stage__num{font-size:30px;font-weight:400;color:var(--sky);line-height:.9}
  .stage__title{font-weight:800;color:var(--blue);font-size:12.5px;letter-spacing:.2px}
  .stage__sub{font-style:italic;font-weight:600;color:var(--sky);font-size:11.5px}
  .stage p{margin-bottom:6px}
  .skills-lead{font-style:italic;font-weight:700;color:var(--sky);font-size:13px;line-height:1.4;margin-bottom:10px}
  .callout{font-style:italic;font-weight:700;color:var(--lime);font-size:13.5px;line-height:1.4;text-align:center;margin:10px 0}
  .inside-right .inside-body{top:30px}
  .inside-right .photo{top:auto;bottom:0;height:250px}
  .testimonial{position:absolute;left:26px;right:26px;bottom:26px;color:var(--white);font-size:11px;line-height:1.45}
  .testimonial__title{font-style:italic;font-weight:700;font-size:14px;text-align:center;margin-bottom:6px;color:var(--lime)}
  .testimonial__by{margin-top:6px;font-weight:700;text-align:right}
</style>
</head>
<body>

<!-- ===== Outside of brochure ===== -->
<section class="spread spread--outside">

  <div class="panel flap">
    <div class="flap__body">
      <h2 class="flap__title">Coaching can help you:</h2>
      <ul class="ticks">
        <li>Feel more in control by being a more collected and calm participant in the legal process</li>
        <li>Stay focused on what is important to you and your family</li>
        <li>Feel more understood and supported during a very difficult time</li>
        <li>Save time and money by being organised and prepared before meetings with lawyers</li>
        <li>Develop a clear parenting plan with your children's needs at the centre</li>
        <li>Communicate more calmly with your former partner</li>
        <li>Build confidence to start a new chapter of your life</li>
      </ul>
      <p class="flap__note">Coaching works well over the phone, by video call or in person — flexible appointments available.</p>
    </div>
    <div class="photo" role="img" aria-label="Photo of a parent walking with two children along a sunny beach at the water's edge"></div>
    <svg class="swoosh" style="bottom:236px" width="360" height="44" viewBox="0 0 360 44" aria-hidden="true">
      <path d="M0 34 Q180 -4 360 30 L360 44 L0 44 Z" fill="#f3fafd" opacity="0"/>
      <path d="M0 40 Q180 4 360 36 L360 44 L0 44 Z" fill="none"/>
    </svg>
  </div>

  <div class="panel back">
    <div class="back__circle" role="img" aria-label="Round photo of a parent hugging two children"></div>
    <div class="back__body">
      <h2 class="section-title">SERVICES</h2>
      <ul class="ticks">
        <li>Specialist divorce support to suit your needs</li>
        <li>Pre-mediation coaching helping you prepare and achieve more positive outcomes to avoid going to court</li>
        <li>Collaborative law coaching to increase your skills so you can participate more constructively in negotiations</li>
        <li>Delivery of HWN Conflict Style Profile giving you feedback on the constructive and destructive behaviours you choose during conflict to make more productive choices</li>
        <li>Corporate Conflict Management Training</li>
      </ul>
    </div>
    <div class="back__foot">
      <svg width="360" height="250" viewBox="0 0 360 250" aria-hidden="true">
        <defs>
          <linearGradient id="backBand" x1="0" y1="0" x2="1" y2="1">
            <stop offset="0" stop-color="#34a7d7"/>
            <stop offset="1" stop-color="#3277b5"/>
          </linearGradient>
        </defs>
        <path d="M0 30 Q180 80 360 20 L360 250 L0 250 Z" fill="#abd037"/>
        <path d="M0 40 Q180 92 360 32 L360 250 L0 250 Z" fill="#ffffff"/>
        <path d="M0 108 Q180 140 360 100 L360 250 L0 250 Z" fill="url(#backBand)"/>
      </svg>
      <div class="badges">
        <span class="badge"><span class="badge__square"></span>HWN</span>
        <span class="badge"><span class="badge__circle"></span>HWT</span>
      </div>
      <div class="contact">
        <div class="contact__name">Contact Margaret Lane</div>
        HWT Certified Divorce Coach<br>
        Mobile 0400 123 456 · hello@calmcrossingcoaching.com.au
      </div>
      <div class="web">www.calmcrossingcoaching.com.au</div>
    </div>
  </div>

  <div class="panel cover">
    <div class="photo" role="img" aria-label="Photo of a smiling mother hugging her young daughter outdoors"></div>
    <div class="brand"><span class="brand__circle"></span>HWT</div>
    <svg class="swoosh" style="top:400px" width="360" height="140" viewBox="0 0 360 140" aria-hidden="true">
      <defs>
        <linearGradient id="coverBand" x1="0" y1="0" x2="1" y2="1">
          <stop offset="0" stop-color="#34a7d7"/>
          <stop offset="1" stop-color="#3277b5"/>
        </linearGradient>
      </defs>
      <path d="M0 120 Q160 110 360 0 L360 140 L0 140 Z" fill="#abd037"/>
      <path d="M0 130 Q170 118 360 14 L360 140 L0 140 Z" fill="#ffffff"/>
      <path d="M0 140 Q180 126 360 28 L360 140 Z" fill="url(#coverBand)"/>
    </svg>
    <div class="cover__text">
      <h1 class="cover__title">SPECIALIST DIVORCE SUPPORT</h1>
      <p class="cover__tag">Helping you move through this major life challenge so you can more successfully start living your new life – your way!</p>
    </div>
    <div class="web">www.calmcrossingcoaching.com.au</div>
  </div>
</section>

<!-- ===== Inside of brochure ===== -->
<section class="spread spread--inside">

  <div class="panel inside-panel">
    <div class="photo photo--sea" role="img" aria-label="Photo of calm ocean water under a pale sky"></div>
    <p class="goals">Together we will identify your goals, set priorities and develop a plan for tomorrow – moving you through the pain of divorce to regain confidence and start anew.</p>
    <div class="inside-body">
      <p class="lead">You will go through distinct stages:</p>
      <div class="stage">
        <div class="stage__head"><span class="stage__num">1</span>
          <div><div class="stage__title">THE PREPARATION STAGE</div><div class="stage__sub">maybe one or two coaching sessions</div></div></div>
        <p>Anticipating all the unknowns and preparing before you see a family law solicitor can save a lot of your time and therefore money. The clearer you are on what you want to achieve, the more focused the process becomes.</p>
      </div>
      <div class="stage">
        <div class="stage__head"><span class="stage__num">2</span>
          <div><div class="stage__title">THE BUSINESS SIDE OF DIVORCE</div><div class="stage__sub">maybe two to four coaching sessions</div></div></div>
        <p>Divorce involves multiple areas of change, intensity of emotions, life-changing decisions, loss of family structure and often a sense of isolation not experienced before. The emotional overwhelm can impact your ability to make well considered decisions.</p>
        <p>Together we will process emotions constructively and clarify decisions to be made – for you to be better able to communicate these in negotiations as well as new boundaries.</p>
      </div>
    </div>
  </div>

  <div class="panel inside-panel">
    <div class="photo photo--family" role="img" aria-label="Photo of a parent and two children walking on the sand at the beach"></div>
    <div class="inside-body">
      <p class="skills-lead">Where necessary we can work on skills you will need for successful outcomes with property settlements and parenting orders e.g.</p>
      <ul class="ticks">
        <li>Conflict resolution skills plus specific verbal and written communication skills important for maintaining respectful conversations</li>
        <li>Managing anger</li>
        <li>Preparing before attending joint conferences or mediation</li>
        <li>Supporting your children to also navigate changes in family structure</li>
        <li>Strategies for you to start healing and become whole again</li>
        <li>Creating a parenting plan to anticipate and address possible parenting issues, leading to more positive and successful co-parenting in the long term</li>
        <li>Grieving losses – even if you are the one who made the decision to leave</li>
        <li>Strategies to sustain your energy levels to make good considered decisions</li>
      </ul>
    </div>
    <svg class="swoosh" style="top:222px;left:-360px;width:720px" width="720" height="40" viewBox="0 0 720 40" aria-hidden="true">
      <path d="M0 30 Q360 -6 720 26 L720 40 L0 40 Z" fill="#abd037"/>
      <path d="M0 36 Q360 4 720 32 L720 40 L0 40 Z" fill="#ffffff"/>
    </svg>
  </div>

  <div class="panel inside-panel inside-right">
    <div class="inside-body">
      <div class="stage">
        <div class="stage__head"><span class="stage__num">3</span>
          <div><div class="stage__title">THE MOVING ON STAGE</div><div class="stage__sub">one or two coaching sessions</div></div></div>
        <p>Building your self-image and focusing on the future:</p>
        <ul class="ticks">
          <li>Changing your "self" image and building self-worth</li>
          <li>Moving from married life to being single again</li>
          <li>Identifying barriers preventing you from moving forward</li>
          <li>Setting realistic goals to help transition to your new life</li>
          <li>Dating again, when you feel ready</li>
        </ul>
      </div>
      <p class="callout">Everyone is different and moves through the stages at their own pace.</p>
      <p>Often family and friends can try to influence decisions based on what they see as best for you, rather than what you truly want. A coach offers an objective and caring space.</p>
      <p style="margin-top:6px">Even the most together and wise can be cloudy during the emotional overwhelm. Support makes the difference.</p>
    </div>
    <div class="photo photo--sunset" role="img" aria-label="Photo of a sunset glowing over the sea"></div>
    <div class="testimonial">
      <p class="testimonial__title">Testimonial</p>
      <p>"After many years of marriage and three children I was lost. Coaching gave me the clarity and calm I needed to make good decisions for my family. I now feel positive about the future and grateful for the support."</p>
      <p class="testimonial__by">Leanne – Bondi, NSW</p>
    </div>
  </div>
</section>

</body>
</html>
```